Orrin Funeral Home stationery
Orrin Funeral Home
Professional
Duncan P. Orrin
Funeral Director
41 Larch St.
Calais, ME 04682
and
58 Mill St.
Eastport, ME 04657
207-516-2870 or 207-739-6152
duncan@orrinfuneralhome.example
www.orrinfuneralhome.example
The Eastport address is the 739 phone number
Logo
Funerals - Cremations - Prearrangements
Logo in eps

```html
<!DOCTYPE html>
<html lang="en">
<head>
<meta charset="utf-8">
<title>Orrin Funeral Home stationery</title>
<link rel="stylesheet" href="https://fonts.googleapis.com/css2?family=Cormorant+Garamond:wght@600&family=Open+Sans:wght@400;600;700&display=swap">
<style>
  :root {
    --navy: #1d3b8c;
    --navy-dark: #102766;
    --ink: #3a3f4a;
    --muted: #8a8f99;
    --paper: #ffffff;
    --ground: #e9e7e3;
    --pillar: #dfe4ee;
  }
  * { box-sizing: border-box; margin: 0; padding: 0; }
  html, body { width: 1200px; height: 897px; overflow: hidden; }
  body {
    background: var(--ground);
    font-family: "Open Sans", sans-serif;
    color: var(--ink);
    position: relative;
  }
  .piece {
    position: absolute;
    background: var(--paper);
    box-shadow: 0 2px 8px rgba(0,0,0,.12);
    overflow: hidden;
  }
  .brand {
    display: flex; align-items: center; gap: 6px;
    font-family: "Cormorant Garamond", serif;
    font-weight: 600;
    color: var(--navy);
    line-height: 1;
  }
  .brand .mark { width: 12px; height: 12px; background: var(--navy); }
  .brand.on-dark { color: #fff; }
  .brand.on-dark .mark { background: #fff; }
  .tagline { font-size: 8px; letter-spacing: .4px; color: var(--navy); }

  /* Business cards */
  .card { width: 270px; height: 154px; border-radius: 8px; }
  .card--front { padding: 18px 16px; display: flex; gap: 14px; }
  .card--front .brand { font-size: 20px; align-self: center; }
  .card--front .details { border-left: 1px solid var(--navy); padding-left: 12px; font-size: 7.5px; line-height: 1.45; }
  .card__name { font-size: 13px; font-weight: 700; color: var(--navy); }
  .card__title { font-size: 8px; color: var(--muted); margin-bottom: 6px; }
  .card--blue { background: linear-gradient(135deg, var(--navy) 0%, var(--navy-dark) 100%); }
  .card--blue, .card--back { display: flex; flex-direction: column; align-items: center; justify-content: center; gap: 10px; }
  .card--blue .brand, .card--back .brand { font-size: 28px; }
  .card--blue .tagline { color: #dbe3f7; }

  /* Envelope & letterhead shared */
  .band { position: absolute; left: 0; right: 0; bottom: 0; background: var(--navy); }
  .band::before { content: ""; position: absolute; left: 0; right: 0; top: -4px; height: 2px; background: #c8cfdc; }
  .pillar { position: absolute; background: linear-gradient(180deg, var(--pillar), #f4f6fa); opacity: .9; }

  .envelope { left: 580px; top: 520px; width: 560px; height: 280px; }
  .envelope .brand { position: absolute; left: 26px; top: 24px; font-size: 26px; }
  .envelope .return { position: absolute; left: 26px; top: 60px; font-size: 8px; line-height: 1.5; color: var(--muted); }
  .envelope .band { height: 14px; }
  .envelope .pillar { right: 60px; top: 30px; width: 120px; height: 226px; }

  .letterhead { left: 60px; top: 150px; width: 460px; height: 600px; }
  .letterhead .brand { position: absolute; left: 36px; top: 32px; font-size: 30px; }
  .letterhead .contact { position: absolute; right: 36px; top: 34px; text-align: right; font-size: 7.5px; line-height: 1.5; color: var(--muted); }
  .letterhead .letter { position: absolute; left: 36px; right: 150px; top: 130px; font-size: 8.5px; line-height: 1.7; }
  .letterhead .letter p { margin-bottom: 12px; }
  .letterhead .signer { font-weight: 600; color: var(--navy); }
  .letterhead .band { height: 18px; }
  .letterhead .pillar { right: 30px; top: 260px; width: 110px; height: 310px; }
</style>
</head>
<body>

  <!-- Business card fronts -->
  <section class="piece card card--front" style="left:580px; top:80px;">
    <div class="brand"><span class="mark"></span>Orrin</div>
    <div class="details">
      <div class="card__name">Duncan P. Orrin</div>
      <div class="card__title">Funeral Director</div>
      <div>41 Larch St., Calais, ME 04682</div>
      <div>58 Mill St., Eastport, ME 04657</div>
      <div>207-516-2870 or 207-739-6152</div>
      <div>duncan@orrinfuneralhome.example</div>
      <div>www.orrinfuneralhome.example</div>
    </div>
  </section>

  <section class="piece card card--blue" style="left:870px; top:80px;">
    <div class="brand on-dark"><span class="mark"></span>Orrin</div>
    <div class="tagline">Funerals - Cremations - Prearrangements</div>
  </section>

  <section class="piece card card--front" style="left:580px; top:260px;">
    <div class="brand"><span class="mark"></span>Orrin</div>
    <div class="details">
      <div class="card__name">Duncan P. Orrin</div>
      <div class="card__title">Funeral Director</div>
      <div>41 Larch St., Calais, ME 04682</div>
      <div>58 Mill St., Eastport, ME 04657</div>
      <div>207-516-2870 or 207-739-6152</div>
      <div>duncan@orrinfuneralhome.example</div>
      <div>www.orrinfuneralhome.example</div>
    </div>
  </section>

  <section class="piece card card--back" style="left:870px; top:260px;">
    <div class="brand"><span class="mark"></span>Orrin</div>
    <div class="tagline">Funerals - Cremations - Prearrangements</div>
  </section>

  <!-- Envelope -->
  <section class="piece envelope">
    <div class="brand"><span class="mark"></span>Orrin Funeral Home</div>
    <div class="return">
      41 Larch St., Calais, ME 04682<br>
      58 Mill St., Eastport, ME 04657
    </div>
    <div class="pillar" role="img" aria-label="Faint pedestal illustration"></div>
    <div class="band"></div>
  </section>

  <!-- Letterhead -->
  <section class="piece letterhead">
    <div class="brand"><span class="mark"></span>Orrin Funeral Home</div>
    <div class="contact">
      41 Larch St., Calais, ME 04682<br>
      58 Mill St., Eastport, ME 04657<br>
      207-516-2870 or 207-739-6152<br>
      www.orrinfuneralhome.example
    </div>
    <div class="letter">
      <p>March 4, 2024</p>
      <p>Recipient Name<br>Street Address<br>Town, State</p>
      <p>Dear Family,</p>
      <p>Thank you for allowing us to serve your family during this difficult time. Our staff remains available to answer any questions about services, arrangements or memorial details. Please call us at any hour.</p>
      <p>With sympathy,</p>
      <p class="signer">Duncan P. Orrin<br><span style="font-weight:400;color:var(--muted)">Funeral Director</span></p>
    </div>
    <div class="pillar" role="img" aria-label="Faint pedestal illustration"></div>
    <div class="band"></div>
  </section>

</body>
</html>
```